Lagoonworks Solutions

I run an aquarium service business covering all aspects of large scale saltwater aquariums. Design, installation, and service. My main customer base is corporations in Manhattan, but I also deal with smaller home or business aquariums in the tri-state area. I work with cutting edge equipment and service techniques and need to convey that.

Industry/Entity Type

Business

Contact Information for Business Card

LAGOONWORKS SOLUTIONS LLC
Jonathan R. Delvoy
Owner
Main 415-555-0182
Cell 415-555-0267
Service.LagoonSolutions@mailbeam.net

```html
<!DOCTYPE html>
<html lang="en">
<head>
<meta charset="utf-8">
<title>Lagoonworks Solutions – Business Card</title>
<link rel="stylesheet" href="https://fonts.googleapis.com/css2?family=Archivo:wght@700&family=Delius&display=swap">
<style>
  :root {
    --backdrop: #1a1c20;
    --card-black: #050608;
    --frame-blue: #2c4a8c;
    --panel-slate: #2a3140;
    --steel: #8ea0b8;
    --text-light: #c9d0da;
    --art-light: #7d8590;
    --art-dark: #0b0c0f;
  }
  * { margin: 0; padding: 0; box-sizing: border-box; }
  html, body {
    width: 1200px; height: 900px; overflow: hidden;
    background: var(--backdrop);
  }
  .canvas { position: relative; width: 1200px; height: 900px; }

  .card { position: absolute; background: var(--card-black); overflow: hidden; }

  /* Front */
  .card-front { left: 70px; top: 267px; width: 640px; height: 366px; }
  .card-front .frame {
    position: absolute; inset: 14px;
    border: 2px solid var(--frame-blue);
  }
  .card-front .artwork {
    position: absolute; left: 56px; top: 42px; width: 140px; height: 290px;
    border-radius: 46% 40% 50% 50% / 30% 30% 60% 60%;
    background: radial-gradient(ellipse at 45% 45%, var(--art-light) 0%, #3c424c 45%, var(--art-dark) 100%);
  }
  .card-front .wordmark {
    position: absolute; left: 212px; top: 56px; width: 396px;
    font-family: "Archivo", Arial, sans-serif; font-weight: 700;
    color: var(--steel); line-height: 1; letter-spacing: -0.5px;
    white-space: nowrap;
  }
  .wordmark .line-main { display: block; font-size: 45px; }
  .wordmark .line-sub { display: block; font-size: 33px; margin-top: 2px; }
  .card-front .contact-panel {
    position: absolute; left: 215px; right: 0; top: 176px; height: 120px;
    background: var(--panel-slate);
  }
  .contact {
    position: absolute; right: 30px; top: 180px; text-align: right;
    font-family: "Delius", "Comic Sans MS", cursive; color: var(--text-light);
  }
  .contact .name { font-size: 19px; margin-bottom: 6px; }
  .contact .row {
    display: flex; justify-content: flex-end; align-items: center; gap: 8px;
    font-size: 14px; margin-bottom: 6px;
  }
  .contact .row.email { font-size: 10.5px; margin-top: 6px; }
  .contact svg { width: 14px; height: 12px; flex: none; }

  /* Back */
  .card-back { left: 770px; top: 130px; width: 366px; height: 640px; }
  .card-back .side-band {
    position: absolute; left: 0; top: 0; width: 92px; height: 100%;
    background: var(--panel-slate);
  }
  .card-back .side-name {
    position: absolute; left: 46px; top: 28px;
    writing-mode: vertical-rl;
    transform: translateX(-50%);
    font-family: "Archivo", Arial, sans-serif; font-weight: 700;
    font-size: 33px; letter-spacing: -0.5px; color: var(--steel);
    white-space: nowrap;
  }
  .card-back .artwork {
    position: absolute; left: 150px; top: 150px; width: 190px; height: 400px;
    border-radius: 46% 40% 50% 50% / 30% 30% 60% 60%;
    background: radial-gradient(ellipse at 45% 42%, var(--art-light) 0%, #3c424c 45%, var(--art-dark) 100%);
  }
</style>
</head>
<body>
<main class="canvas">

  <section class="card card-front">
    <div class="frame"></div>
    <div class="artwork" role="img" aria-label="Seahorse sculpted from mechanical aquarium parts"></div>
    <h1 class="wordmark">
      <span class="line-main">LAGOONWORKS</span>
      <span class="line-sub">SOLUTIONS LLC</span>
    </h1>
    <div class="contact-panel"></div>
    <div class="contact">
      <p class="name">Jonathan R. Delvoy</p>
      <p class="row">415-555-0182
        <svg viewBox="0 0 14 12" aria-hidden="true"><path d="M1 4 Q7 0 13 4 L11 6 L9 4.5 L5 4.5 L3 6 Z M4 6 H10 L12 11 H2 Z" fill="none" stroke="currentColor" stroke-width="1"/></svg>
      </p>
      <p class="row">415-555-0267
        <svg viewBox="0 0 14 12" aria-hidden="true"><rect x="4.5" y="1" width="5" height="10" rx="1" fill="none" stroke="currentColor" stroke-width="1"/></svg>
      </p>
      <p class="row email">Service.LagoonSolutions@mailbeam.net
        <svg viewBox="0 0 14 12" aria-hidden="true"><rect x="1" y="2" width="12" height="8" fill="none" stroke="currentColor" stroke-width="1"/><path d="M1 2 L7 7 L13 2" fill="none" stroke="currentColor" stroke-width="1"/></svg>
      </p>
    </div>
  </section>

  <section class="card card-back">
    <div class="side-band"></div>
    <p class="side-name">LAGOONWORKS SOLUTIONS LLC</p>
    <div class="artwork" role="img" aria-label="Seahorse sculpted from mechanical aquarium parts"></div>
  </section>

</main>
</body>
</html>
```